Bright Mesh Business Card

This is a business card for a printing company but I actually don't have a logo. Just need to typeset the words "Bright Mesh Printing" as the logo. Then add my name "Loretta Vance" + phone number + address

Target Market(s)

ceos and professionals

Industry/Entity Type

printing and manufacturing

Contact Information for Business Card

Bright Mesh Printing/ 4617 calloway st. Alder Grove, CA 91648/ 555-417-3980/ Loretta Vance

Font styles to use
Serif
Other font styles liked:
• a modern font would be nice

Colors
0054AA
0677BA
7BADD7
CADEEF
E8F1F8
0094D4
00A9DD
6FCCEA
C7EBF8
E9F6FB

Requirements
Must have
• company name, number, address
Nice to have
• nice bold feel
Should not have
• nothing in particular

```html
<!DOCTYPE html>
<html lang="en">
<head>
<meta charset="utf-8">
<title>Bright Mesh Printing — Business Card</title>
<link rel="stylesheet" href="https://fonts.googleapis.com/css2?family=Bebas+Neue&family=Arimo:wght@400&display=swap">
<style>
  :root {
    --backdrop: #171717;
    --kraft-light: #dfbf95;
    --kraft-mid: #c89f6e;
    --kraft-dark: #a4764a;
    --ink: #0e0b08;
  }
  * { margin: 0; padding: 0; box-sizing: border-box; }
  html, body {
    width: 1093px;
    height: 1200px;
    overflow: hidden;
    background: var(--backdrop);
  }
  .canvas {
    position: relative;
    width: 1093px;
    height: 1200px;
  }
  .card {
    position: absolute;
    left: 265px;
    width: 580px;
    height: 357px;
    background: linear-gradient(150deg, var(--kraft-light) 0%, var(--kraft-mid) 55%, var(--kraft-dark) 100%);
    color: var(--ink);
    text-align: center;
  }
  .card--front { top: 226px; }
  .card--back {
    top: 620px;
    display: flex;
    align-items: center;
    justify-content: center;
  }
  .holder-name {
    position: absolute;
    top: 95px;
    left: 0;
    right: 0;
    font-family: "Bebas Neue", sans-serif;
    font-weight: 400;
    font-size: 42px;
    line-height: 1;
  }
  .divider {
    position: absolute;
    left: 253px;
    width: 74px;
    height: 1px;
    background: var(--ink);
  }
  .divider--upper { top: 144px; }
  .divider--lower { top: 198px; }
  .phone, .address {
    position: absolute;
    left: 0;
    right: 0;
    font-family: "Arimo", sans-serif;
    font-size: 18px;
    line-height: 23px;
  }
  .phone { top: 161px; }
  .address { top: 213px; }
  .company-name {
    font-family: "Bebas Neue", sans-serif;
    font-weight: 400;
    font-size: 58px;
    line-height: 1;
  }
</style>
</head>
<body>
  <main class="canvas">
    <section class="card card--front">
      <h1 class="holder-name">Loretta Vance</h1>
      <div class="divider divider--upper"></div>
      <p class="phone">555-417-3980</p>
      <div class="divider divider--lower"></div>
      <p class="address">4617 calloway st. Alder<br>Grove, CA 91648</p>
    </section>
    <section class="card card--back">
      <p class="company-name">Bright Mesh Printing</p>
    </section>
  </main>
</body>
</html>
```